Business Card Design for Translation Company - Rush

Rush job for a business card designing for a company doing international translations, several Asian and western languages. Already have a logo design (see attached) to use as the basis of the business card design. For the card, we also need the full company name, address, email, and phone number. In addition, my name as I will be the one handing out the cards.

For the logo design, we think the white background would be best. But we will consider using the dark background if you have a great idea for it.

The attached jpeg design has just been approved, but the designer has not yet finalized the file. When we select our final applicant, we will send the finalized file. (Nothing changes except the quality of the data.)

The phone number may change and if so, we will send the new one when we select our applicant.

We must complete the entire process and have a design ready to go to print no later than 01:00 am August 3, New York (East Coast) time.

We look forward to your participation in the project,
Jon

Target Market(s)

Translation clients worldwide.

Industry/Entity Type

Business

Contact Information for Business Card

Company details:

Korvane Translations International, Ltd.

#276-3820 Welbury Crescent, Victoria, BC, Canada V9T4K2

jhadley@korvanetranslations-example.com

+1-888-647-2315

Font styles to use
Sans Serif

Requirements
Must have
• Company name, address, email and phone number.
• Also my name:
• Jonathan R. Hadley
• Director
Nice to have
• Not a demand, but please consider creatively using the horizontal bar.
Should not have
• Cluttered of jumbled appearance.

```html
<!DOCTYPE html>
<html lang="en">
<head>
<meta charset="utf-8">
<title>Korvane Translations – Business Card</title>
<link rel="stylesheet" href="https://fonts.googleapis.com/css2?family=Open+Sans:ital,wght@0,400;0,600;0,700;1,400&display=swap">
<style>
  :root {
    --orange: #ee7623;
    --ink: #3a3a3a;
    --white: #ffffff;
    --black: #1b1b1c;
    --stage: #ecebe8;
    --card-w: 700px;
    --card-h: 400px;
  }
  * { box-sizing: border-box; margin: 0; padding: 0; }
  html, body {
    width: 1200px; height: 1024px; overflow: hidden;
    background: var(--stage);
    font-family: "Open Sans", Arial, sans-serif;
  }
  .sheet {
    width: 1200px; height: 1024px;
    display: flex; flex-direction: column; align-items: center; justify-content: center;
    gap: 44px;
  }
  .card {
    position: relative;
    width: var(--card-w); height: var(--card-h);
    overflow: hidden;
    box-shadow: 0 6px 18px rgba(0,0,0,.14);
  }
  .card--front { background: var(--white); }
  .card--back { background: var(--black); }

  .card__shape { position: absolute; inset: 0; }

  .brand {
    position: absolute; display: flex; align-items: center; gap: 16px;
  }
  .brand__dot {
    width: 38px; height: 38px; border-radius: 50%;
    background: var(--orange); flex: none;
  }
  .brand__name {
    font-weight: 600; letter-spacing: .28em; font-size: 19px; line-height: 1.35;
    text-transform: uppercase;
  }
  .brand__rule {
    display: block; height: 2px; width: 120px; background: var(--orange);
    margin-top: 8px;
  }
  .card--front .brand { left: 44px; bottom: 58px; }
  .card--front .brand__name { color: var(--ink); }
  .card--back .brand { left: 190px; top: 150px; }
  .card--back .brand__name { color: var(--white); }

  .contact {
    position: absolute; left: 430px; top: 70px; width: 250px;
    color: var(--white);
  }
  .contact__name { font-weight: 700; font-size: 17px; text-transform: uppercase; letter-spacing: .02em; }
  .contact__title { font-size: 13px; margin-bottom: 26px; }
  .contact__line { font-size: 10.5px; line-height: 1.6; }
  .contact__group { margin-bottom: 16px; }

  .website {
    position: absolute; left: 44px; bottom: 36px;
    font-size: 13px; font-style: italic; color: var(--white);
  }
  .website__name { color: var(--orange); }
</style>
</head>
<body>
<main class="sheet">
  <article class="card card--front">
    <svg class="card__shape" viewBox="0 0 700 400" aria-hidden="true">
      <path fill="var(--orange)" d="M250 0 H700 V400 H440 C370 320 330 210 338 112 L292 138 Z"/>
    </svg>
    <div class="brand">
      <span class="brand__dot"></span>
      <div>
        <div class="brand__name">Korvane<br>Translations</div>
        <span class="brand__rule"></span>
      </div>
    </div>
    <div class="contact">
      <p class="contact__name">Jonathan R. Hadley</p>
      <p class="contact__title">Director</p>
      <div class="contact__group">
        <p class="contact__line">P : +1-888-647-2315</p>
        <p class="contact__line">E : jhadley@korvanetranslations-example.com</p>
      </div>
      <div class="contact__group">
        <p class="contact__line">Korvane Translations International, Ltd.</p>
        <p class="contact__line">#276-3820 Welbury Crescent,</p>
        <p class="contact__line">Victoria, BC, Canada V9T4K2</p>
      </div>
    </div>
  </article>

  <article class="card card--back">
    <div class="brand">
      <span class="brand__dot"></span>
      <div>
        <div class="brand__name">Korvane<br>Translations</div>
        <span class="brand__rule"></span>
      </div>
    </div>
    <p class="website">www.<span class="website__name">korvanetranslations-example</span>.com</p>
  </article>
</main>
</body>
</html>
```